Creating a label for germicidal disposable wipes.

I need to create a label to put on our containers of germicidal disposable wipes. I am attaching an example of another germicidal wipe that I would like a similar format but more customized to look like my companies.

```html
<!DOCTYPE html>
<html lang="en">
<head>
<meta charset="utf-8">
<title>CleanMed Germicidal Wipes Label</title>
<link href="https://fonts.googleapis.com/css2?family=Barlow:wght@400;500;600;700;800&family=Open+Sans:wght@400&display=swap" rel="stylesheet">
<style>
  :root {
    --navy: #272a78;
    --ink: #111111;
    --charcoal: #3a3a3a;
    --green: #2fb04a;
    --teal: #1c7f86;
    --white: #ffffff;
    --stage: #eceded;
  }
  * { margin: 0; padding: 0; box-sizing: border-box; }
  html, body { width: 1200px; height: 870px; overflow: hidden; background: var(--stage); }
  .label {
    position: absolute; left: 20px; top: 49px; width: 1160px; height: 772px;
    border-radius: 26px; overflow: hidden; display: flex; background: var(--white);
  }
  .label__front { position: relative; width: 646px; height: 100%; padding: 28px 0 0 52px; }
  .brand { display: flex; align-items: center; gap: 14px; height: 112px; }
  .brand__mark { width: 76px; height: 76px; border-radius: 50%; background: var(--teal); flex: none; }
  .brand__name {
    font-family: "Barlow", sans-serif; font-weight: 700; color: var(--charcoal);
    font-size: 30px; line-height: 1.05; text-transform: uppercase;
  }
  .brand__division {
    font-family: "Barlow", sans-serif; font-weight: 500; color: var(--navy);
    font-size: 17px; letter-spacing: .5px; margin-top: 4px;
  }
  .product__name {
    font-family: "Barlow", sans-serif; font-weight: 800; color: var(--ink);
    font-size: 84px; line-height: 1; margin-top: 8px; letter-spacing: -1px;
  }
  .product__type {
    font-family: "Barlow", sans-serif; font-weight: 700; color: var(--navy);
    font-size: 56px; line-height: 1; margin-top: 4px;
  }
  .product__rule {
    width: 456px; height: 8px; margin-top: 12px;
    background: linear-gradient(90deg, var(--green), var(--teal) 45%, var(--navy));
  }
  .badges { display: flex; gap: 18px; margin-top: 26px; margin-left: -10px; }
  .badge { width: 152px; height: 152px; }
  .claim {
    font-family: "Barlow", sans-serif; font-weight: 700; color: var(--navy);
    font-size: 14.5px; margin-top: 30px; letter-spacing: .1px;
  }
  .directions {
    font-family: "Open Sans", sans-serif; font-size: 14px; line-height: 20px;
    color: var(--ink); width: 466px; text-align: justify; margin-top: 10px;
  }
  .directions__lead { font-family: "Barlow", sans-serif; font-size: 20px; text-transform: uppercase; }
  .label__info {
    position: relative; flex: 1; padding: 156px 40px 0 43px; color: var(--white);
    background: linear-gradient(150deg, var(--navy) 0%, #283a86 25%, var(--teal) 48%, var(--navy) 62%, #1f7d78 82%, var(--green) 100%);
    font-family: "Barlow", sans-serif; font-size: 20px; line-height: 26px; letter-spacing: .2px;
  }
  .label__pattern { position: absolute; inset: 0; background: radial-gradient(circle at 85% 12%, rgba(40,200,170,.35), transparent 30%), radial-gradient(circle at 15% 88%, rgba(60,200,140,.3), transparent 28%); }
  .info__body { position: relative; }
  .info__title { font-weight: 600; text-transform: uppercase; margin-bottom: 26px; }
  .info__block { margin-bottom: 15px; }
  .info__block strong { font-weight: 600; }
</style>
</head>
<body>
<main class="label">
  <section class="label__front">
    <header class="brand">
      <span class="brand__mark"></span>
      <div>
        <div class="brand__name">Kestrel Refuse Systems</div>
        <div class="brand__division">HAZARDOUS DIVISION</div>
      </div>
    </header>
    <h1 class="product__name">CleanMed</h1>
    <h2 class="product__type">Germicidal Wipes</h2>
    <div class="product__rule"></div>

    <div class="badges">
      <svg class="badge" viewBox="0 0 152 152" aria-label="Disinfects in 2 minutes">
        <defs><path id="arcA" d="M 28 76 A 48 48 0 0 1 124 76"/></defs>
        <circle cx="76" cy="76" r="72" fill="var(--navy)"/>
        <circle cx="76" cy="76" r="64" fill="var(--white)"/>
        <circle cx="76" cy="76" r="45" fill="var(--navy)"/>
        <text font-family="Barlow, sans-serif" font-weight="700" font-size="15" fill="var(--navy)"><textPath href="#arcA" startOffset="50%" text-anchor="middle">DISINFECTS IN</textPath></text>
        <text x="76" y="92" text-anchor="middle" font-family="Barlow, sans-serif" font-weight="800" font-size="52" fill="var(--white)">2</text>
        <text x="76" y="110" text-anchor="middle" font-family="Barlow, sans-serif" font-weight="600" font-size="12" fill="var(--white)">MINUTES</text>
      </svg>
      <svg class="badge" viewBox="0 0 152 152" aria-label="Not a skin or baby wipe">
        <defs><path id="arcB" d="M 26 90 A 52 52 0 1 1 126 90"/></defs>
        <circle cx="76" cy="76" r="72" fill="var(--navy)"/>
        <circle cx="76" cy="76" r="64" fill="var(--white)"/>
        <circle cx="76" cy="80" r="40" fill="var(--navy)" role="img" aria-label="Wipe package icon"/>
        <line x1="50" y1="54" x2="102" y2="106" stroke="var(--white)" stroke-width="6"/>
        <text font-family="Barlow, sans-serif" font-weight="700" font-size="14" fill="var(--navy)"><textPath href="#arcB" startOffset="50%" text-anchor="middle">NOT A SKIN OR BABY WIPE</textPath></text>
      </svg>
      <svg class="badge" viewBox="0 0 152 152" aria-label="Do not flush">
        <defs><path id="arcC" d="M 30 70 A 48 48 0 0 1 122 70"/></defs>
        <circle cx="76" cy="76" r="72" fill="var(--navy)"/>
        <circle cx="76" cy="76" r="64" fill="var(--white)"/>
        <circle cx="76" cy="84" r="40" fill="var(--navy)" role="img" aria-label="Toilet icon"/>
        <line x1="50" y1="58" x2="102" y2="110" stroke="var(--white)" stroke-width="6"/>
        <text font-family="Barlow, sans-serif" font-weight="700" font-size="15" fill="var(--navy)"><textPath href="#arcC" startOffset="50%" text-anchor="middle">DO NOT FLUSH</textPath></text>
      </svg>
    </div>

    <p class="claim">BACTERICIDAL, TUBERCULOCIDAL, AND VIRUCIDAL* IN 2 MINUTES</p>
    <p class="directions">Lorem ipsum dolor sit amet, consectetuer adipiscing elit, sed diam nonummy nibh euismod tincidunt ut laoreet dolore magna aliquam erat volutpat. Ut wisi enim ad minim veniam, quis nostrud exerci tation ullamcorper suscipit lobortis nisl ut aliquip ex ea commodo consequat. Duis autem vel eum iriure dolor in hendrerit in vulputate velit esse molestie consequat <span class="directions__lead">Vel illum dolore eu feugiat nulla</span> facilisis at vero eros et accumsan et iusto odio dignissim qui blandit facilisi.</p>
  </section>

  <section class="label__info">
    <div class="label__pattern" role="img" aria-label="Faint decorative shapes in teal and green"></div>
    <div class="info__body">
      <p class="info__title">Lorem ipsum dolor sit amet,</p>
      <p class="info__block"><strong>CONSECTETUER</strong> adipiscing elit, sed diam nonummy nibh euismod tincidunt ut laoreet dolore magna aliquam erat volutpat.</p>
      <p class="info__block"><strong>UT WISI ENIM</strong> ad minim veniam, quis nostrud exerci tation ullamcorper suscipit lobortis nisl ut aliquip ex ea commodo consequat.</p>
      <p class="info__block"><strong>DUIS AUTEM VEL EUM</strong> iriure dolor in hendrerit in vulputate velit esse molestie consequat, vel illum dolore eu feugiat nulla facilisis at vero eros et accumsan et iusto odio dignissim qui blandit praesent luptatum zzril delenit augue.</p>
      <p class="info__block"><strong>DUIS AUTEM</strong> vel eum iriure dolor in hendrerit in vulputate velit esse molestie consequat, vel illum dolore eu feugiat nulla facilisis at vero eros et accumsan et iusto odio dignissim qui blandit praesent luptatum zzril delenit augue duis dolore te feugait nulla facilisi.</p>
    </div>
  </section>
</main>
</body>
</html>
```